4" x 6" Coffee Label for a Fundraising Project

You will be designing a full-color label for a coffee product.
This particular design is for a school band fundraising program, and should align with the school existing webiste in terms of 'look and feel.'
You may choose any one of the following coffee blends to build your design around: Lantern Meadow, sumatra, hazelnut, Quiet Interlude, mocha, Harvest March, Peppermint Carol or cinnabun. (Yes, we will need multiple labels in the near future.) Your design for a label should be expandable to other coffee varieties and leverage some brand elements across different labels to reflect brand consistency.
What is the brand? It is a k-12 school, the fundraisor is for the school's music / band program. The primary colors are red, white and black; however you should incorporate other colors that represent the coffee blend (from the above list).
Who is the target market? Coffee drinkers! (So your design should reflect the positive qualities of coffee) They are also parents, friends and alumni of the school.
What is the brand's feel? Your design should bring to mind the following when drinkers view the label on the package: high quality, a luxury drink, aligned with christian values, perhaps a sense of community, and the school's band and/or performing arts. (Please note that this design is specific to the band program.)
Can I create a name for any of the above blends that has band connetations? Yes! Actually, ideating band-related names is encouraged. If your design uses Lantern Meadow or Copper Ballad for the Lantern Meadow, or Tawny Tango or Velvet Fanfare for the mocha blend - AWESOME! So get creative in renaming the blends appropraitely and incorporating this into your overall design. Even better if your naming convention and design could be leveraged across several different coffee blends.
If you incorporate photo imagery in your design, note that we will need to procure similar images we own or can license. Thus, photo imagery should be FPO and representative of they type of imagery for the design.
Specifications for the design are:
1. 4" wide x 6" tall portrait layout
2. 1600 x 2400 pixes
3. CYML for printing
4. Note that the bottom third must be left completely clean - no design elements or text - for NQB required labeling.
5. Design must be completed in Adobe Photoshop or Illustrator.
6. All incorporated fonts must be available for use without licensing.

```html
<!DOCTYPE html>
<html lang="en">
<head>
<meta charset="utf-8">
<title>Harbor Pines Band Coffee Labels</title>
<link rel="stylesheet" href="https://fonts.googleapis.com/css2?family=Montserrat:wght@700;800;900&display=swap">
<style>
  :root {
    --backdrop: #cc1530;
    --brand-red: #cb1a2e;
    --white: #ffffff;
    --ink: #111111;
    --breakfast: #8a3a1e;
    --sumatra: #3bb5b4;
    --hazelnut: #9a4aa8;
    --decaf: #32b6e2;
    --mocha: #e09a78;
    --pumpkin: #f5873a;
    --candy: #e8202a;
  }
  * { margin: 0; padding: 0; box-sizing: border-box; }
  html, body { width: 1200px; height: 722px; overflow: hidden; }
  body { background: var(--backdrop); font-family: "Montserrat", sans-serif; position: relative; }

  .label {
    position: absolute; width: 170px; height: 254px;
    background: var(--white); overflow: hidden;
    box-shadow: 0 4px 8px rgba(0,0,0,.25);
  }
  /* Design area ends at 169px; the bottom third stays blank for required labeling */
  .label__band {
    position: absolute; left: 0; right: 0; top: 136px; height: 33px;
    background: var(--brand-red);
  }
  .label__band::after {
    content: ""; position: absolute; left: 0; right: 0; bottom: 0; height: 5px;
    background: var(--accent);
  }

  .brand-tab {
    position: absolute; left: 64px; top: 0; width: 42px; height: 38px;
    background: var(--brand-red);
    display: flex; flex-direction: column; align-items: center; justify-content: center; gap: 3px;
  }
  .brand-tab__dot { width: 7px; height: 7px; border-radius: 50%; background: var(--ink); }
  .brand-tab__name { color: var(--white); font-weight: 700; font-size: 4.6px; letter-spacing: .2px; white-space: nowrap; }

  .title {
    position: absolute; left: 0; right: 0; top: 50px;
    text-align: center; color: var(--ink);
    font-weight: 900; font-size: 19px; line-height: 19px; letter-spacing: -.3px;
  }
  .title--compact { font-size: 16px; }
  .title__sub {
    display: block; margin-top: 4px;
    color: var(--brand-red); font-weight: 800; font-size: 6px; line-height: 7px; letter-spacing: 0;
  }

  .info {
    position: absolute; left: 14px; top: 112px; width: 142px; height: 46px;
    background: var(--accent);
  }
  .info::before {
    content: ""; position: absolute; left: 0; right: 0; top: 0; height: 3px;
    background: radial-gradient(circle at 50% 0, var(--white) 2px, transparent 2.4px) repeat-x;
    background-size: 6px 3px;
  }
  .info__table {
    position: absolute; left: 8px; top: 7px; width: 126px; height: 32px;
    border: .7px solid var(--white);
    display: grid; grid-template-columns: 7px 36px 49px 1fr;
  }
  .info__notes {
    background: var(--white); color: var(--ink);
    writing-mode: vertical-rl; transform: rotate(180deg);
    font-weight: 700; font-size: 4px; text-align: center;
  }
  .info__keys, .info__values { display: grid; grid-template-rows: repeat(4, 1fr); border-right: .7px solid var(--white); }
  .info__keys span, .info__values span {
    color: var(--white); display: flex; align-items: center; padding-left: 3px;
    border-bottom: .5px solid var(--white); white-space: nowrap;
  }
  .info__keys span:last-child, .info__values span:last-child { border-bottom: 0; }
  .info__keys span { font-size: 2.8px; font-weight: 700; }
  .info__values span { font-size: 4px; font-weight: 700; }
  .info__seal { display: flex; align-items: center; justify-content: center; }
  .info__seal svg { width: 24px; height: 24px; }
</style>
</head>
<body>

<article class="label" style="left:88px;top:89px;--accent:var(--breakfast)">
  <div class="label__band"></div>
  <div class="brand-tab"><span class="brand-tab__dot"></span><span class="brand-tab__name">HARBOR PINES</span></div>
  <h2 class="title">LANTERN<br>MEADOW<span class="title__sub">ROASTED COFFEE</span></h2>
  <div class="info"><div class="info__table">
    <div class="info__notes">NOTES</div>
    <div class="info__keys"><span>ROAST</span><span>REGION</span><span>ROASTED COFFEE</span><span>ROASTING DATE</span></div>
    <div class="info__values"><span>MEDIUM</span><span>COLUMBIA</span><span>500 G</span><span>11.12.2024</span></div>
    <div class="info__seal"><svg viewBox="0 0 24 24"><circle cx="12" cy="12" r="10" fill="none" stroke="#fff" stroke-width="1"/></svg></div>
  </div></div>
</article>

<article class="label" style="left:294px;top:89px;--accent:var(--sumatra)">
  <div class="label__band"></div>
  <div class="brand-tab"><span class="brand-tab__dot"></span><span class="brand-tab__name">HARBOR PINES</span></div>
  <h2 class="title">ISLAND<br>OVERTURE<span class="title__sub">ROASTED COFFEE</span></h2>
  <div class="info"><div class="info__table">
    <div class="info__notes">NOTES</div>
    <div class="info__keys"><span>ROAST</span><span>REGION</span><span>ROASTED COFFEE</span><span>ROASTING DATE</span></div>
    <div class="info__values"><span>MEDIUM</span><span>COLUMBIA</span><span>500 G</span><span>11.12.2024</span></div>
    <div class="info__seal"><svg viewBox="0 0 24 24"><circle cx="12" cy="12" r="10" fill="none" stroke="#fff" stroke-width="1"/></svg></div>
  </div></div>
</article>

<article class="label" style="left:499px;top:89px;--accent:var(--hazelnut)">
  <div class="label__band"></div>
  <div class="brand-tab"><span class="brand-tab__dot"></span><span class="brand-tab__name">HARBOR PINES</span></div>
  <h2 class="title">HAZEL<br>HARMONY<span class="title__sub">ROASTED COFFEE</span></h2>
  <div class="info"><div class="info__table">
    <div class="info__notes">NOTES</div>
    <div class="info__keys"><span>ROAST</span><span>REGION</span><span>ROASTED COFFEE</span><span>ROASTING DATE</span></div>
    <div class="info__values"><span>MEDIUM</span><span>COLUMBIA</span><span>500 G</span><span>11.12.2024</span></div>
    <div class="info__seal"><svg viewBox="0 0 24 24"><circle cx="12" cy="12" r="10" fill="none" stroke="#fff" stroke-width="1"/></svg></div>
  </div></div>
</article>

<article class="label" style="left:88px;top:378px;--accent:var(--decaf)">
  <div class="label__band"></div>
  <div class="brand-tab"><span class="brand-tab__dot"></span><span class="brand-tab__name">HARBOR PINES</span></div>
  <h2 class="title title--compact">QUIET<br>INTERLUDE<span class="title__sub">ROASTED COFFEE</span></h2>
  <div class="info"><div class="info__table">
    <div class="info__notes">NOTES</div>
    <div class="info__keys"><span>ROAST</span><span>REGION</span><span>ROASTED COFFEE</span><span>ROASTING DATE</span></div>
    <div class="info__values"><span>MEDIUM</span><span>COLUMBIA</span><span>500 G</span><span>11.12.2024</span></div>
    <div class="info__seal"><svg viewBox="0 0 24 24"><circle cx="12" cy="12" r="10" fill="none" stroke="#fff" stroke-width="1"/></svg></div>
  </div></div>
</article>

<article class="label" style="left:294px;top:378px;--accent:var(--mocha)">
  <div class="label__band"></div>
  <div class="brand-tab"><span class="brand-tab__dot"></span><span class="brand-tab__name">HARBOR PINES</span></div>
  <h2 class="title">VELVET<br>FANFARE<span class="title__sub">ROASTED COFFEE</span></h2>
  <div class="info"><div class="info__table">
    <div class="info__notes">NOTES</div>
    <div class="info__keys"><span>ROAST</span><span>REGION</span><span>ROASTED COFFEE</span><span>ROASTING DATE</span></div>
    <div class="info__values"><span>MEDIUM</span><span>COLUMBIA</span><span>500 G</span><span>11.12.2024</span></div>
    <div class="info__seal"><svg viewBox="0 0 24 24"><circle cx="12" cy="12" r="10" fill="none" stroke="#fff" stroke-width="1"/></svg></div>
  </div></div>
</article>

<article class="label" style="left:499px;top:378px;--accent:var(--pumpkin)">
  <div class="label__band"></div>
  <div class="brand-tab"><span class="brand-tab__dot"></span><span class="brand-tab__name">HARBOR PINES</span></div>
  <h2 class="title">HARVEST<br>MARCH<span class="title__sub">ROASTED COFFEE</span></h2>
  <div class="info"><div class="info__table">
    <div class="info__notes">NOTES</div>
    <div class="info__keys"><span>ROAST</span><span>REGION</span><span>ROASTED COFFEE</span><span>ROASTING DATE</span></div>
    <div class="info__values"><span>MEDIUM</span><span>COLUMBIA</span><span>500 G</span><span>11.12.2024</span></div>
    <div class="info__seal"><svg viewBox="0 0 24 24"><circle cx="12" cy="12" r="10" fill="none" stroke="#fff" stroke-width="1"/></svg></div>
  </div></div>
</article>

<article class="label" style="left:823px;top:234px;--accent:var(--candy)">
  <div class="label__band"></div>
  <div class="brand-tab"><span class="brand-tab__dot"></span><span class="brand-tab__name">HARBOR PINES</span></div>
  <h2 class="title title--compact">PEPPERMINT<br>CAROL<span class="title__sub">ROASTED COFFEE</span></h2>
  <div class="info"><div class="info__table">
    <div class="info__notes">NOTES</div>
    <div class="info__keys"><span>ROAST</span><span>REGION</span><span>ROASTED COFFEE</span><span>ROASTING DATE</span></div>
    <div class="info__values"><span>MEDIUM</span><span>COLUMBIA</span><span>500 G</span><span>11.12.2024</span></div>
    <div class="info__seal"><svg viewBox="0 0 24 24"><circle cx="12" cy="12" r="10" fill="none" stroke="#fff" stroke-width="1"/></svg></div>
  </div></div>
</article>

</body>
</html>
```